Natural Skincare Product Labels Design

We are looking for a designer to create elegant but quirky, functional product labels for our natural skincare range.
The labels must reflect our brand’s values of simplicity, luxury, and the natural, handmade essence of our products.
https://www.instagram.com/tolvarenskincare
1. Key Details
Packaging Dimensions
Container Types: Transparent jars.
Sizes for Body Products:
Diameter: 64mm–68mm.
Heights: 80mm, 88mm, and 97mm (lid height: 15mm).
Sizes for Face Creams:
Diameter: 60mm.
Height: 50mm (lid height: 15mm).
Label Fit: For body products, ideally one label size to fit all jar sizes.
For the smaller face cream jars, a separate, tailored label is required.
2. Label Placement
Options include a wrapped-around label or a combination of wrapped-around and top-of-jar elements.
Transparent jars mean the label must leave space for the product to be visible (e.g., partial wrap or cutout areas).
3. Content Requirements
Product Name: Prominently displayed.
Ingredient List: Dedicated space required.
Disclaimer/Usage Instructions: Include space for this information.
4. Design Goals
Look & Feel: Simple, upmarket, and natural, with a handmade essence.
Logo Usage: Our logo is finalized and available in gold, black, and white variants. Use Josefin Bold font for the logo if adjustments are required.
Color Palette: Neutral tones (e.g., whites, blacks, golds) are preferred, with flexibility for subtle pops of color tied to each product’s main ingredient.
5. Imagery
Open to including images and colours (e.g., botanical illustrations) that highlight the main ingredient (e.g., coffee beans, turmeric root, or honeycomb). Also open to labels having a prominent colour to tie it in to the main ingredient.
Alternatively, no images can also work for a clean design.
6. Current Design Context
Our temporary design features gold leaf on top and a simple handmade side label. We’re seeking to elevate this to a more polished, cohesive design.
7. Product Line
- Body Products (Larger Jars)
Mivo Body Butter
Key Ingredients: Guarana & Cupuaçu butter (inspired by Brazil).
Note: “Mivo” is slang for “bum.”
Manuka Honey Body Butter
Key Ingredients: Manuka honey (from New Zealand) & Cupuaçu butter.
Coffee Body Scrub
Key Ingredients: Coffee and Demerara sugar.
Whipped Body Soap - Turmeric
Key Ingredients: Turmeric and Bentonite clay.
Whipped Body Soap - Banana
- Face Products (Smaller Jars)
Face Cream
Key Ingredients: Carrot Oil and Raspberry Oil.
Features natural UV protection.
Good Night Cream
Key Ingredients: Enriched with Magnesium.
Promotes relaxation and restful sleep.
8. Submission Guidelines
Flexibility: Design should allow for consistent branding across all products while accommodating the varying jar sizes and ingredient focus.
Material Considerations: Labels should complement the transparent jars and allow the product inside to remain partially visible.
Print Elements: Incorporating gold accents is a plus but should not overpower the design.
We’re excited to see your vision for a label that celebrates the natural beauty and high quality of our skincare range. Please include mockups to showcase the design in use, particularly on transparent jars of varying sizes.
women 20-50 years of age

```html
<!DOCTYPE html>
<html lang="en">
<head>
<meta charset="utf-8">
<title>Tolvaren Body Butter Labels</title>
<link href="https://fonts.googleapis.com/css2?family=Federo&family=Josefin+Sans:wght@400;700&family=Poppins:wght@400&display=swap" rel="stylesheet">
<style>
  :root {
    --page: #f3f0eb;
    --cream: #fdf3d9;
    --cream-soft: #fbe9b8;
    --gold: #c99a3a;
    --gold-text: #b88c3f;
    --guarana-red: #c21f32;
    --honey-orange: #f28a1a;
    --ink: #2a2a2a;
    --muted: #8a7a5a;
  }
  * { margin: 0; padding: 0; box-sizing: border-box; }
  html, body { width: 1200px; height: 1200px; overflow: hidden; }
  body {
    background: var(--page);
    font-family: "Poppins", sans-serif;
    color: var(--ink);
    position: relative;
  }
  .label {
    position: absolute;
    top: 400px;
    width: 530px;
    height: 400px;
    background: var(--cream);
    border-top: 9px solid var(--gold);
    border-bottom: 9px solid var(--gold);
    overflow: hidden;
  }
  .label--mivo { left: 45px; }
  .label--manuka { left: 625px; }
  .side-text {
    position: absolute;
    top: 12px;
    height: 364px;
    writing-mode: vertical-rl;
    font-family: "Poppins", sans-serif;
    font-size: 9px;
    letter-spacing: 0.3px;
    color: var(--muted);
  }
  .side-text--left { left: 6px; }
  .side-text--right { right: 6px; }
  .brand {
    position: absolute;
    left: 0; right: 0;
    top: 110px;
    text-align: center;
    font-family: "Josefin Sans", sans-serif;
    font-weight: 400;
    font-size: 21px;
    letter-spacing: 5px;
    color: var(--gold-text);
  }
  .brand-dot {
    display: block;
    width: 34px; height: 34px;
    margin: 0 auto 14px;
    border: 1.5px solid var(--gold-text);
    border-radius: 50%;
  }
  .brand--mivo { top: 52px; }
  .brand--manuka { top: 46px; }
  .product-name {
    position: absolute;
    left: 0; right: 0;
    text-align: center;
    font-family: "Federo", sans-serif;
    line-height: 1;
  }
  .product-name--mivo {
    top: 150px;
    font-size: 44px;
    color: var(--guarana-red);
  }
  .product-name--manuka {
    top: 140px;
    font-size: 42px;
    color: var(--honey-orange);
  }
  .product-name--manuka .sub { display: block; font-size: 36px; margin-top: 6px; }
  .art {
    position: absolute;
    border-radius: 40%;
  }
  .art--guarana {
    left: 125px; top: 210px;
    width: 280px; height: 120px;
    background: radial-gradient(ellipse at 55% 55%, #d8432a 0 35%, #5da43a 60%, rgba(93,164,58,0) 72%);
  }
  .art--flower-left {
    left: 70px; top: 230px;
    width: 120px; height: 100px;
    background: radial-gradient(ellipse, rgba(242,138,26,0.45), rgba(242,138,26,0) 70%);
  }
  .art--flower-right {
    right: 70px; top: 230px;
    width: 120px; height: 100px;
    background: radial-gradient(ellipse, rgba(242,138,26,0.45), rgba(242,138,26,0) 70%);
  }
  .art--drop {
    left: 250px; top: 262px;
    width: 30px; height: 48px;
    border-radius: 50% 50% 50% 50% / 60% 60% 40% 40%;
    background: linear-gradient(#f6a53a, #e8780e);
  }
  .ingredients {
    position: absolute;
    left: 0; right: 0;
    text-align: center;
    font-size: 18px;
  }
  .ingredients--mivo { top: 332px; }
  .ingredients--manuka { top: 322px; }
  .volume {
    position: absolute;
    left: 0; right: 0;
    text-align: center;
    font-size: 20px;
  }
  .volume--mivo { top: 355px; }
  .volume--manuka { top: 347px; }
</style>
</head>
<body>
  <section class="label label--mivo">
    <p class="side-text side-text--left">After shower body butter made with love</p>
    <p class="side-text side-text--right">INGREDIENTS: Shea butter, Mango butter, Cupuaçu butter, Guarana extract.</p>
    <div class="brand brand--mivo"><span class="brand-dot"></span>TOLVAREN</div>
    <h1 class="product-name product-name--mivo">Mivo Body Butter</h1>
    <div class="art art--guarana" role="img" aria-label="Illustration of guarana fruits with green leaves"></div>
    <p class="ingredients ingredients--mivo">Guarana &amp; Cupuaçu butter</p>
    <p class="volume volume--mivo">250ml</p>
  </section>

  <section class="label label--manuka">
    <p class="side-text side-text--left">After shower body butter made with cupuaçu butter keeps skin soft</p>
    <div class="brand brand--manuka"><span class="brand-dot"></span>TOLVAREN</div>
    <h1 class="product-name product-name--manuka">Manuka Honey<span class="sub">Body Butter</span></h1>
    <div class="art art--flower-left" role="img" aria-label="Line drawing of a manuka flower"></div>
    <div class="art art--drop" role="img" aria-label="Honey drop illustration"></div>
    <div class="art art--flower-right" role="img" aria-label="Line drawing of a manuka flower"></div>
    <p class="ingredients ingredients--manuka">Manuka Honey &amp; Cupuaçu butter</p>
    <p class="volume volume--manuka">250ml</p>
  </section>
</body>
</html>
```